Larkspur Homes - wanted BRILLIANT website design for our new property investing company

We need a website design for our new company based in Bristol, England, UK called "Larkspur Homes". We help buy people property who are in financial difficulty or who are needing to sell their property quickly for reasons such as death, divorce/separation, relocation, emigration.

We have a logo being designed incorporating strawberry and property (so red and green). We would like designs to communicate an elegant ,professional, approachable, friendly
fresh clean but also warm appealing appearance
Not too busy
Website consistent with logo and company name i.e. colour scheme

Please use our word document for content as a guide but use professional judgement for minor alterations if you feel they would benefit the site/structure etc

Please ask at any time if not sure

Target Market(s)

Adult british population, those that have a mortgage / loan / own property

Industry/Entity Type

Financial

Font styles to use
Serif
Sans Serif
Decorative

Colors
0692cd
33b7a4
acd036
fbee3e
3176b5
886aae
a6479a
e567a6
eb1f27

Requirements
Must have
• This must not look like a template website we are looking for UNIQUE please!
Nice to have
• Bristol pictures instead of generic, or colourful line drawings/comic drawings of houses/property/keys/happy people.....
Should not have
• An obvious off the shelf template design

```html
<!DOCTYPE html>
<html lang="en">
<head>
<meta charset="utf-8">
<title>Larkspur Homes</title>
<link rel="stylesheet" href="https://fonts.googleapis.com/css2?family=Open+Sans:wght@400&family=Tinos:wght@400&display=swap">
<style>
:root{
  --red:#f3424f;
  --red-soft:#f27a80;
  --sky:#55d6ee;
  --sky-light:#7fd8f8;
  --lime:#c1cf06;
  --orange:#fb8651;
  --text-blue:#7ccfe9;
  --white:#ffffff;
  --ink:#333333;
  --logo-red:#c8232f;
}
*{margin:0;padding:0;box-sizing:border-box}
html,body{width:984px;height:1200px;overflow:hidden;background:var(--white)}
body{position:relative;font-family:"Open Sans",Arial,sans-serif;color:var(--ink)}
.abs{position:absolute}

.top-band{left:0;top:0;width:984px;height:93px;background:linear-gradient(180deg,var(--red) 0%,var(--red-soft) 70%,var(--red) 100%)}
.logo-arc{left:90px;top:0;width:230px;height:127px;background:var(--white);border-radius:115px 115px 0 0}
.logo-name{left:90px;top:94px;width:230px;text-align:center;font-family:"Tinos",Georgia,serif;font-size:25px;color:var(--logo-red)}
.logo-dot{left:188px;top:28px;width:34px;height:34px;border-radius:50%;background:var(--logo-red)}
.social{right:0;top:0}
.social-flag{left:757px;top:0;width:33px;height:50px}
.social-dot{top:12px;width:14px;height:14px;border-radius:50%;background:var(--white)}

.main-nav{left:89px;top:136px;width:819px;height:39px;background:var(--sky);border-radius:6px;display:flex;align-items:center}
.main-nav a{position:absolute;color:var(--white);font-size:11.5px;text-decoration:none;top:12px;white-space:nowrap}

.hero{top:189px;height:351px}
.hero-1{left:89px;width:272px;background:linear-gradient(160deg,#3f5d5a,#a9b7a6 35%,#7a6a3a 75%,#b09b55);border-radius:3px 0 0 3px}
.hero-2{left:361px;width:275px;background:linear-gradient(160deg,#9aa629,#e1c98e 45%,#c59357 80%,#8a8a2a)}
.hero-3{left:636px;width:273px;background:linear-gradient(160deg,#3d4c24,#c99070 45%,#d7b48c 70%,#3b4a78);border-radius:0 3px 3px 0}

.card{top:563px;width:264px;height:136px;border-radius:6px;color:var(--white)}
.card-green{left:88px;background:var(--lime)}
.card-blue{left:367px;background:var(--sky-light)}
.card-orange{left:643px;background:var(--orange)}
.card-icon{position:absolute;left:16px;top:8px;width:56px;height:56px;border-radius:8px;background:rgba(255,255,255,.25)}
.card-title{position:absolute;left:105px;top:11px;font-family:"Tinos",Georgia,serif;font-size:20px;line-height:21px}
.card-text{position:absolute;left:15px;top:79px;width:240px;font-family:"Tinos",Georgia,serif;font-size:12.3px;line-height:16.5px}

.welcome-photo{left:89px;top:731px;width:258px;height:184px;border-radius:6px;background:linear-gradient(135deg,#2f4a44,#8e6a52 40%,#d9a88c 60%,#6b5440)}
.welcome-title{left:372px;top:729px;font-family:"Tinos",Georgia,serif;font-size:24.5px;color:var(--text-blue)}
.welcome-text{left:372px;top:781px;width:430px;font-family:"Tinos",Georgia,serif;font-size:12.2px;line-height:21.3px;color:var(--text-blue)}
.read-more{left:699px;top:881px;width:105px;height:26px;border-radius:5px;background:var(--sky-light);font-family:"Tinos",Georgia,serif;font-size:11.5px;color:var(--ink);text-align:center;line-height:26px}

.site-footer{left:0;top:943px;width:984px;height:257px;background:linear-gradient(180deg,var(--red) 0%,var(--red-soft) 55%,var(--red-soft) 85%,var(--red) 100%);color:var(--white)}
.footer-title{position:absolute;top:24px;font-family:"Tinos",Georgia,serif;font-size:24.5px}
.quick-links{position:absolute;left:93px;top:58px;list-style:none;font-size:10.8px;line-height:19.7px}
.quick-links li{display:flex;align-items:center}
.quick-links svg{width:12px;height:8px;margin-right:16px}
.about-text{position:absolute;left:329px;top:58px;width:340px;font-size:10.8px;line-height:19.7px}
.field{position:absolute;left:694px;width:129px;height:23px;background:var(--white);border-radius:4px;font-family:"Tinos",Georgia,serif;font-size:11.5px;color:#e8a5a0;padding:3px 11px}
.field-text{width:210px;height:48px}
.submit{position:absolute;left:845px;top:184px;width:57px;height:23px;border-radius:4px;background:var(--white);font-family:"Tinos",Georgia,serif;font-size:10px;color:#e8a5a0;text-align:center;line-height:23px}
.footer-rule{position:absolute;left:89px;top:216px;width:819px;height:1px;background:rgba(255,255,255,.5)}
.copyright{position:absolute;right:77px;top:230px;font-family:"Tinos",Georgia,serif;font-size:10.5px}
</style>
</head>
<body>

<header>
  <div class="abs top-band"></div>
  <div class="abs logo-arc"></div>
  <div class="abs logo-dot"></div>
  <div class="abs logo-name">Larkspur Homes</div>

  <svg class="abs social-flag" viewBox="0 0 33 50" aria-label="Social link"><polygon points="0,0 33,0 33,40 16.5,50 0,40" fill="#8ee3f7"/><circle cx="16.5" cy="19" r="7" fill="#ffffff"/></svg>
  <div class="abs social-dot" style="left:806px" aria-label="Social link"></div>
  <div class="abs social-dot" style="left:840px" aria-label="Social link"></div>
  <svg class="abs" style="left:876px;top:12px;width:14px;height:14px" viewBox="0 0 14 14" aria-label="More"><path d="M7 1v12M1 7h12" stroke="#ffffff" stroke-width="2.4"/></svg>

  <nav class="abs main-nav">
    <a style="left:23px">HOME</a>
    <a style="left:96px">SELL YOUR PROPERTY FAST</a>
    <a style="left:282px">RENY YOUR PROPERTY FAST</a>
    <a style="left:477px">COMMIN QUESTIONS</a>
    <a style="left:633px">ABOUT US</a>
    <a style="left:731px">CONTACT</a>
  </nav>
</header>

<section>
  <div class="abs hero hero-1" role="img" aria-label="Photo of a woman stretching her arms in an open meadow"></div>
  <div class="abs hero hero-2" role="img" aria-label="Photo of a mother lifting her baby outdoors"></div>
  <div class="abs hero hero-3" role="img" aria-label="Photo of a smiling family with their dog"></div>
</section>

<section>
  <div class="abs card card-green">
    <div class="card-icon" role="img" aria-label="Handshake icon"></div>
    <div class="card-title">Mission &amp;<br>Services</div>
    <p class="card-text">Lorem ipsum dolor sit amet conse ctetur adipi-sicing elit, sed do eiusmod tempor incididunt ut labore et dolore magna aliqua....&gt;&gt;&gt;</p>
  </div>
  <div class="abs card card-blue">
    <div class="card-icon" role="img" aria-label="Speech bubble icon"></div>
    <div class="card-title" style="left:85px">Make<br>Donations</div>
    <p class="card-text">Lorem ipsum dolor sit amet conse ctetur adipi-sicing elit, sed do eiusmod tempor incididunt ut labore et dolore magna aliqua...&gt;&gt;&gt;</p>
  </div>
  <div class="abs card card-orange">
    <div class="card-icon" role="img" aria-label="Light bulb icon"></div>
    <div class="card-title" style="left:76px">Our<br>Programs</div>
    <p class="card-text" style="top:74px">Lorem ipsum dolor sit amet conse ctetur adipi-sicing elit, sed do eiusmod tempor incididunt ut labore et dolore magna aliqua...&gt;&gt;&gt;</p>
  </div>
</section>

<section>
  <div class="abs welcome-photo" role="img" aria-label="Portrait photo of a smiling young girl"></div>
  <h1 class="abs welcome-title" style="font-weight:400">Welcome to oue site !</h1>
  <p class="abs welcome-text">Lorem Ipsum is simply dummy text of the printing and typesetting industry. Lorem Ipsum has been the industry's standard dummy text ever since the 1500s, when an unknown printer took a galley of type and scrambled it to make a type specimen book. It has survived not only five centuries</p>
  <div class="abs read-more">Read More...</div>
</section>

<footer class="abs site-footer">
  <h2 class="footer-title" style="left:91px;font-weight:400">Quick links</h2>
  <ul class="quick-links">
    <li><svg viewBox="0 0 12 8"><path d="M1 4l3 3 7-6" stroke="#fff" stroke-width="1.6" fill="none"/></svg>Aenean nonummy</li>
    <li><svg viewBox="0 0 12 8"><path d="M1 4l3 3 7-6" stroke="#fff" stroke-width="1.6" fill="none"/></svg>Fusce suscipit varius mi</li>
    <li><svg viewBox="0 0 12 8"><path d="M1 4l3 3 7-6" stroke="#fff" stroke-width="1.6" fill="none"/></svg>Hendrerit mauris phasellus</li>
    <li><svg viewBox="0 0 12 8"><path d="M1 4l3 3 7-6" stroke="#fff" stroke-width="1.6" fill="none"/></svg>Praesent vestibulum molestie</li>
    <li><svg viewBox="0 0 12 8"><path d="M1 4l3 3 7-6" stroke="#fff" stroke-width="1.6" fill="none"/></svg>Praesent vestibulum molestie</li>
    <li><svg viewBox="0 0 12 8"><path d="M1 4l3 3 7-6" stroke="#fff" stroke-width="1.6" fill="none"/></svg>Hendrerit mauris phasellus</li>
  </ul>

  <h2 class="footer-title" style="left:329px;font-weight:400">About Us</h2>
  <p class="about-text">Contrary to popular belief, Lorem Ipsum is not simply random text. It has roots in a piece of classical Latin literature from 45 BC, making it over 2000 years old. Edwin Harrow, Etiam a odio nec mi convallis malesuada&nbsp; Nam iaculis pharetra purus quis venenatis</p>

  <h2 class="footer-title" style="left:693px;font-weight:400">CONTACT</h2>
  <div class="field" style="top:64px">Name*</div>
  <div class="field" style="top:95px">E-mail *</div>
  <div class="field field-text" style="top:126px">Text *</div>
  <div class="submit">Submit</div>

  <div class="footer-rule"></div>
  <div class="copyright">Larkspur Homes &nbsp;© 2014 All Rights Reserved</div>
</footer>

</body>
</html>
```